Criação de Papelaria Profissional para Limpeza & Serviço para o lar
A empresa queria:
" Terceirizamos serviços de limpeza empresarial, portaria, recepção, copeira, limpeza pós-obra "

```html
<!DOCTYPE html>
<html lang="pt-BR">
<head>
<meta charset="UTF-8">
<title>LarClaro — Papelaria</title>
<link href="https://fonts.googleapis.com/css2?family=Nunito:wght@700&family=Arimo:wght@400;700&display=swap" rel="stylesheet">
<style>
  :root {
    --backdrop: #ece8e2;
    --paper: #ffffff;
    --brand-blue: #3c6fa6;
    --brand-green: #8cc63f;
    --ink: #3a3a3a;
    --photo-light: #e9ece6;
    --photo-mid: #b9c2b4;
    --photo-dark: #7d8a86;
  }
  * { margin: 0; padding: 0; box-sizing: border-box; }
  html, body { width: 1200px; height: 1200px; overflow: hidden; }
  body {
    background: var(--backdrop);
    position: relative;
    font-family: "Arimo", Arial, sans-serif;
  }
  .brand-tile {
    position: absolute;
    left: 451px; top: 187px;
    width: 262px; height: 268px;
    background: var(--paper);
    display: flex; align-items: center; justify-content: center; gap: 10px;
  }
  .brand-name {
    font-family: "Nunito", Arial, sans-serif;
    font-weight: 700;
    color: var(--brand-blue);
    letter-spacing: -0.5px;
  }
  .brand-tile .brand-name { font-size: 44px; }
  .brand-dot {
    display: block; border-radius: 50%;
    background: var(--brand-green);
  }
  .brand-tile .brand-dot { width: 26px; height: 26px; }

  .banner {
    position: absolute;
    left: 0; top: 516px;
    width: 1200px; height: 468px;
    background: var(--paper);
  }
  .banner-photo {
    position: absolute; left: 0; top: 0;
    width: 700px; height: 100%;
    background: linear-gradient(90deg, var(--photo-mid) 0%, var(--photo-dark) 35%, var(--photo-light) 75%, var(--paper) 100%);
  }
  .banner-edge {
    position: absolute; right: 0; top: 0;
    width: 24px; height: 100%;
    background: var(--brand-blue);
  }
  .banner-info {
    position: absolute; left: 712px; top: 0;
    width: 420px; height: 100%;
  }
  .banner-info .brand-line {
    position: absolute; left: 0; top: 180px;
    display: flex; align-items: center; gap: 14px;
  }
  .banner-info .brand-name { font-size: 80px; line-height: 1; }
  .banner-info .brand-dot { width: 40px; height: 40px; }
  .contact {
    position: absolute; left: 0;
    display: flex; align-items: center; gap: 18px;
    color: var(--ink);
    font-size: 19px; line-height: 1.15;
    text-transform: uppercase;
  }
  .contact-phone { top: 305px; }
  .contact-web { top: 365px; font-weight: 700; }
  .contact svg { width: 28px; height: 28px; flex: none; }
</style>
</head>
<body>
  <div class="brand-tile">
    <span class="brand-dot"></span>
    <span class="brand-name">LarClaro</span>
  </div>

  <section class="banner">
    <div class="banner-photo" role="img" aria-label="Fotografia de equipe de limpeza e recepção uniformizada"></div>
    <div class="banner-info">
      <div class="brand-line">
        <span class="brand-name">LarClaro</span>
        <span class="brand-dot"></span>
      </div>
      <div class="contact contact-phone">
        <svg viewBox="0 0 24 24" aria-hidden="true"><path fill="var(--brand-green)" d="M6.6 10.8a15.2 15.2 0 0 0 6.6 6.6l2.2-2.2a1 1 0 0 1 1-.25 11.4 11.4 0 0 0 3.6.57 1 1 0 0 1 1 1V20a1 1 0 0 1-1 1A17 17 0 0 1 3 4a1 1 0 0 1 1-1h3.5a1 1 0 0 1 1 1c0 1.25.2 2.45.57 3.57a1 1 0 0 1-.25 1z"/></svg>
        <div>00 0000.00000<br>00 0000.00000</div>
      </div>
      <div class="contact contact-web">
        <svg viewBox="0 0 24 24" aria-hidden="true"><circle cx="12" cy="12" r="10" fill="var(--brand-green)"/><path d="M2 12h20M12 2c3 3 3 17 0 20M12 2c-3 3-3 17 0 20" stroke="#fff" stroke-width="1.4" fill="none"/></svg>
        <div>larclaroservicos.com.br<br>contato@larclaroservicos.com.br</div>
      </div>
    </div>
    <div class="banner-edge"></div>
  </section>
</body>
</html>
```